Business Card

we need a logo designed for a company that has been in business since 1985
it is called "Corvan Hydraulics & Haulage Repairs Pty Ltd"
We repair Earthmoving machines (big machines used on mine sites)
We also sell parts to suit them and would like the back of the card to show our brands we sell.
This is a new card for out parts manager we need it designed for her to hand out in business meetings to drive more parts sales
Website details
and contact details are essential

Marlo, Vintane & Broad blade logos on the back are priorities
Secondary Pellum Structures, Hartsvoor

Target Market(s)

This is for the mining industry
Mechanical repairs

Industry/Entity Type

Business

Requirements
Must have
• Company Name: Corvan Hydraulics & Haulage (this logo to be on the front please)
Company message:"Call us in for your next breakdown
Can we make these changable for other staff?
Name: Delia Brandt
Job Title: Parts Manager
Phone: (07) 4610 8274
Fax: (07) 4610 3357
Email: parts@corvanhyd.com.au
Address: 7b Tamberly Street (PO Box 6458) Kelbrook QLD 4736
www.corvanhyd.com.au
Nice to have
• Written on there
New & used parts to suit all types of machinery
Service - Repairs- Overhauls- Labour hire

I would like to get them printed with Quillpress so can you please follow there guidelines
http://www.quillpress-example.com.au/qp/ns/propath/UploadResources.aspx?selectedTab=0?pfid=B99&pf_id=B99&xnav=product-page#FileFormats
Should not have
• Any tooling photos,

```html
<!DOCTYPE html>
<html lang="en">
<head>
<meta charset="utf-8">
<title>Corvan Hydraulics &amp; Haulage – Business Cards</title>
<link href="https://fonts.googleapis.com/css2?family=Open+Sans:ital,wght@0,300;0,400;0,600;1,400&family=Roboto+Condensed:wght@300;400;700&display=swap" rel="stylesheet">
<style>
  :root {
    --page-light: #f4f4f4;
    --page-dark: #d9d9d9;
    --card-black: #08090b;
    --card-charcoal: #1b1e23;
    --icon-blue: #2aa3e3;
    --text-white: #ffffff;
    --text-soft: #d8dbe0;
    --brand-gold: #f5a623;
    --accent-red: #c8102e;
    --ink: #1a1a1a;
    --paper: #ffffff;
  }
  * { box-sizing: border-box; margin: 0; padding: 0; }
  html, body { width: 1200px; height: 691px; overflow: hidden; }
  body {
    position: relative;
    background: radial-gradient(ellipse at 50% 40%, var(--page-light), var(--page-dark));
    font-family: "Open Sans", sans-serif;
  }
  .card {
    position: absolute;
    width: 503px;
    height: 304px;
    overflow: hidden;
    background: linear-gradient(180deg, var(--card-black) 0%, var(--card-charcoal) 55%, var(--card-black) 100%);
    box-shadow: 6px 10px 18px rgba(0,0,0,.35);
    color: var(--text-white);
  }
  .card--delia { left: 62px; top: 28px; }
  .card--owen { left: 635px; top: 28px; }
  .card--back { left: 62px; top: 360px; background: var(--paper); }
  .card--reid { left: 635px; top: 360px; }

  .flare {
    position: absolute;
    left: 0; right: 0;
    height: 40px;
    background:
      radial-gradient(ellipse 22% 6% at 50% 50%, rgba(255,255,255,.95), transparent 100%),
      radial-gradient(ellipse 48% 10% at 50% 50%, rgba(61,155,255,.85), transparent 100%),
      radial-gradient(ellipse 60% 40% at 50% 50%, rgba(61,155,255,.22), transparent 100%);
  }
  .card--delia .flare, .card--owen .flare, .card--reid .flare { top: 164px; }

  .brand-mark {
    position: absolute;
    left: 28px; top: 22px;
    width: 110px; height: 133px;
    display: flex; align-items: center; gap: 5px;
  }
  .brand-mark__square { width: 11px; height: 11px; background: var(--brand-gold); flex: none; }
  .brand-mark__name {
    font-family: "Roboto Condensed", sans-serif;
    font-weight: 700;
    font-size: 23px;
    color: var(--brand-gold);
  }
  .company-name {
    position: absolute;
    left: 146px; top: 68px;
    font-family: "Roboto Condensed", sans-serif;
    font-weight: 300;
    font-size: 16px;
    line-height: 26.5px;
    color: var(--text-soft);
  }
  .person { position: absolute; left: 293px; top: 66px; }
  .person__name { font-weight: 300; font-size: 24px; line-height: 30px; }
  .person__title { font-size: 14px; letter-spacing: 1.4px; }

  .contact { position: absolute; font-size: 13.5px; line-height: 18.5px; color: var(--text-soft); }
  .contact--address { left: 28px; top: 227px; }
  .contact--lines { left: 293px; }
  .card--delia .contact--lines { top: 227px; }
  .card--owen .contact--lines, .card--reid .contact--lines { top: 208px; }
  .contact__row { display: flex; align-items: center; gap: 5px; white-space: nowrap; }
  .contact__row--indent { padding-left: 17px; }
  .contact__strong { font-weight: 600; color: var(--text-white); font-size: 14px; }
  .icon { width: 12px; height: 12px; fill: var(--icon-blue); flex: none; }

  .back-band {
    position: absolute; left: 0; top: 0; right: 0; height: 66px;
    background: linear-gradient(180deg, var(--card-black), var(--card-charcoal));
  }
  .card--back .flare { top: 12px; }
  .tagline {
    position: absolute; left: 106px; top: 58px;
    background: var(--paper);
    padding: 1px 8px;
    font-style: italic;
    font-size: 13.5px;
    letter-spacing: .4px;
    color: var(--ink);
    text-transform: uppercase;
    white-space: nowrap;
  }
  .parts-line {
    position: absolute; left: 0; right: 0; top: 96px;
    text-align: center;
    font-size: 19.5px;
    color: var(--accent-red);
  }
  .services {
    position: absolute; left: 0; right: 0; top: 160px;
    text-align: center;
    font-family: "Roboto Condensed", sans-serif;
    font-size: 21px;
    color: var(--ink);
  }
  .brands {
    position: absolute; left: 24px; right: 22px; top: 248px;
    display: flex; justify-content: space-between; align-items: center;
  }
  .brand {
    display: flex; align-items: center; gap: 4px;
    font-family: "Roboto Condensed", sans-serif;
    font-weight: 700; font-size: 15px; color: var(--ink);
  }
  .brand__square { width: 10px; height: 10px; flex: none; }
  .brand--marlo .brand__square { background: #d2232a; }
  .brand--vintane .brand__square { background: #0b8a3c; }
  .brand--broad .brand__square { background: #f08a1c; }
  .brand--pellum .brand__square { background: #c62828; }
  .brand--hartsvoor .brand__square { background: #2e9e48; }
</style>
</head>
<body>

<svg width="0" height="0" style="position:absolute" aria-hidden="true">
  <symbol id="i-pin" viewBox="0 0 12 12"><path d="M6 0a4.2 4.2 0 0 0-4.2 4.2C1.8 7.4 6 12 6 12s4.2-4.6 4.2-7.8A4.2 4.2 0 0 0 6 0zm0 5.8a1.6 1.6 0 1 1 0-3.2 1.6 1.6 0 0 1 0 3.2z"/></symbol>
  <symbol id="i-globe" viewBox="0 0 12 12"><path d="M6 0a6 6 0 1 0 0 12A6 6 0 0 0 6 0zm4.6 5.3H8.4a9 9 0 0 0-.8-3.6 4.7 4.7 0 0 1 3 3.6zM6 1.3c.6.8 1.1 2.2 1.2 4H4.8c.1-1.8.6-3.2 1.2-4zM4.4 1.7a9 9 0 0 0-.8 3.6H1.4a4.7 4.7 0 0 1 3-3.6zM1.4 6.7h2.2a9 9 0 0 0 .8 3.6 4.7 4.7 0 0 1-3-3.6zM6 10.7c-.6-.8-1.1-2.2-1.2-4h2.4c-.1 1.8-.6 3.2-1.2 4zm1.6-.4a9 9 0 0 0 .8-3.6h2.2a4.7 4.7 0 0 1-3 3.6z"/></symbol>
  <symbol id="i-phone" viewBox="0 0 12 12"><path d="M2.4 0 4.3 2.3 3.2 3.8a7.5 7.5 0 0 0 5 5l1.5-1.1L12 9.6 10.6 11.6C5 11.6.4 7 .4 1.4z"/><path d="M7 1a4 4 0 0 1 4 4h-1a3 3 0 0 0-3-3zm0 2a2 2 0 0 1 2 2H8a1 1 0 0 0-1-1z"/></symbol>
  <symbol id="i-mobile" viewBox="0 0 12 12"><path d="M3 0h6a1 1 0 0 1 1 1v10a1 1 0 0 1-1 1H3a1 1 0 0 1-1-1V1a1 1 0 0 1 1-1zm0 1.5v8h6v-8z"/></symbol>
  <symbol id="i-fax" viewBox="0 0 12 12"><path d="M3 0h5l1 1v3H3zM1 5h10a1 1 0 0 1 1 1v5H0V6a1 1 0 0 1 1-1zm1 2v1h2V7zm3 0v1h2V7zm3 0v1h2V7zM2 9v1h2V9zm3 0v1h2V9zm3 0v1h2V9z"/></symbol>
  <symbol id="i-mail" viewBox="0 0 12 12"><path d="M0 2h12v8H0zm1 1v.4l5 3.3 5-3.3V3zm0 1.6V9h10V4.6L6 7.9z"/></symbol>
</svg>

<section class="card card--delia">
  <div class="flare"></div>
  <div class="brand-mark"><span class="brand-mark__square"></span><span class="brand-mark__name">CORVAN</span></div>
  <p class="company-name">Corvan Hydraulics &amp;<br>Haulage<br>Repairs Pty Ltd</p>
  <div class="person">
    <p class="person__name">Delia Brandt</p>
    <p class="person__title">Parts Manager</p>
  </div>
  <div class="contact contact--address">
    <p class="contact__row"><svg class="icon"><use href="#i-pin"/></svg>7b Tamberly Street (PO Box 6458)</p>
    <p class="contact__row contact__row--indent">Kelbrook QLD 4736</p>
    <p class="contact__row contact__strong"><svg class="icon"><use href="#i-globe"/></svg>www.corvanhyd.com.au</p>
  </div>
  <div class="contact contact--lines">
    <p class="contact__row contact__strong"><svg class="icon"><use href="#i-phone"/></svg>(07) 4610 8274</p>
    <p class="contact__row"><svg class="icon"><use href="#i-fax"/></svg>(07) 4610 3357</p>
    <p class="contact__row"><svg class="icon"><use href="#i-mail"/></svg>parts@corvanhyd.com.au</p>
  </div>
</section>

<section class="card card--owen">
  <div class="flare"></div>
  <div class="brand-mark"><span class="brand-mark__square"></span><span class="brand-mark__name">CORVAN</span></div>
  <p class="company-name">Corvan Hydraulics &amp;<br>Haulage<br>Repairs Pty Ltd</p>
  <div class="person">
    <p class="person__name">Owen Brandt</p>
    <p class="person__title">Director</p>
  </div>
  <div class="contact contact--address">
    <p class="contact__row"><svg class="icon"><use href="#i-pin"/></svg>7b Tamberly Street (PO Box 6458)</p>
    <p class="contact__row contact__row--indent">Kelbrook QLD 4736</p>
    <p class="contact__row contact__strong"><svg class="icon"><use href="#i-globe"/></svg>www.corvanhyd.com.au</p>
  </div>
  <div class="contact contact--lines">
    <p class="contact__row contact__strong"><svg class="icon"><use href="#i-phone"/></svg>(07) 4610 8274</p>
    <p class="contact__row"><svg class="icon"><use href="#i-mobile"/></svg>0407 519 306</p>
    <p class="contact__row"><svg class="icon"><use href="#i-fax"/></svg>(07) 4610 3357</p>
    <p class="contact__row"><svg class="icon"><use href="#i-mail"/></svg>owen@corvanhyd.com.au</p>
  </div>
</section>

<section class="card card--back">
  <div class="back-band"><div class="flare"></div></div>
  <p class="tagline">Call us in for your next breakdown</p>
  <p class="parts-line">New &amp; used parts to suit all types of machinery</p>
  <p class="services">Service&nbsp; •&nbsp; Repairs&nbsp; •&nbsp; Overhauls&nbsp; •&nbsp; Labour hire</p>
  <div class="brands">
    <span class="brand brand--marlo"><span class="brand__square"></span>MARLO</span>
    <span class="brand brand--vintane"><span class="brand__square"></span>Vintane</span>
    <span class="brand brand--broad"><span class="brand__square"></span>Broad Blade Parts</span>
    <span class="brand brand--pellum"><span class="brand__square"></span>Pellum</span>
    <span class="brand brand--hartsvoor"><span class="brand__square"></span>Hartsvoor</span>
  </div>
</section>

<section class="card card--reid">
  <div class="flare"></div>
  <div class="brand-mark"><span class="brand-mark__square"></span><span class="brand-mark__name">CORVAN</span></div>
  <p class="company-name">Corvan Hydraulics &amp;<br>Haulage<br>Repairs Pty Ltd</p>
  <div class="person">
    <p class="person__name">Reid Calloway</p>
    <p class="person__title">Workshop Manager</p>
  </div>
  <div class="contact contact--address">
    <p class="contact__row"><svg class="icon"><use href="#i-pin"/></svg>7b Tamberly Street (PO Box 6458)</p>
    <p class="contact__row contact__row--indent">Kelbrook QLD 4736</p>
    <p class="contact__row contact__strong"><svg class="icon"><use href="#i-globe"/></svg>www.corvanhyd.com.au</p>
  </div>
  <div class="contact contact--lines">
    <p class="contact__row contact__strong"><svg class="icon"><use href="#i-phone"/></svg>(07) 4610 8274</p>
    <p class="contact__row"><svg class="icon"><use href="#i-mobile"/></svg>0400 264 817</p>
    <p class="contact__row"><svg class="icon"><use href="#i-fax"/></svg>(07) 4610 3357</p>
    <p class="contact__row"><svg class="icon"><use href="#i-mail"/></svg>service@corvanhyd.com.au</p>
  </div>
</section>

</body>
</html>
```